Rehearsal studio business card design needed

My rehearsal studio i bought not that long ago was opened as a hobby originally and was definitely not taken seriously. I am trying to make the new look studio be launched with the new look business cards. I am looking for very simple and clean look cards to match the simple and clean studios. the colour scheme is red and grey. over all i am really just looking for a very simple card that is not too busy and just gets the point accross.
Target Market(s)
Targeting bands, music teachers, students, etc.
Industry/Entity Type
Business
Contact Information for Business Card
Bellwater Sound Centre
Rehearsal and Recording Facilities
Owen Taft CEO
unit 8, 47 Marlow Street Penfield NSW 2093
0438 915 264
bellwatersoundcentre@quillmail.example
Requirements
Must have
- simplicity
Nice to have
- black background using the 'white.png' file

```html
<!DOCTYPE html>
<html lang="en">
<head>
<meta charset="utf-8">
<title>Bellwater Sound Centre – Business Card</title>
<link rel="stylesheet" href="https://fonts.googleapis.com/css2?family=Michroma&family=Exo+2:wght@300;400&display=swap">
<style>
  :root {
    --canvas-bg: #2b2b2b;
    --card-bg: #050505;
    --white: #f4f4f4;
    --grey: #9a9a9a;
    --red: #c8202a;
    --card-shadow: rgba(0, 0, 0, 0.55);
  }
  * { box-sizing: border-box; margin: 0; padding: 0; }
  html, body {
    width: 1200px;
    height: 900px;
    overflow: hidden;
    background: var(--canvas-bg);
  }
  .stage {
    position: relative;
    width: 1200px;
    height: 900px;
  }
  .card {
    position: absolute;
    width: 540px;
    height: 310px;
    background: var(--card-bg);
    box-shadow: 0 10px 30px var(--card-shadow);
    overflow: hidden;
  }
  .card--front { left: 50px; top: 390px; }
  .card--back { left: 610px; top: 200px; }

  /* Front */
  .front-brand {
    position: absolute;
    left: 150px;
    top: 150px;
    display: flex;
    align-items: center;
    gap: 14px;
  }
  .brand-dot {
    width: 26px;
    height: 26px;
    border-radius: 50%;
    background: var(--red);
    flex: none;
  }
  .brand-name {
    font-family: "Michroma", sans-serif;
    color: var(--white);
    font-size: 20px;
    letter-spacing: 0.5px;
    white-space: nowrap;
  }

  /* Back */
  .back-heading {
    position: absolute;
    right: 28px;
    top: 28px;
    text-align: right;
    font-family: "Michroma", sans-serif;
    color: var(--white);
    font-size: 14px;
    line-height: 1.55;
  }
  .back-brand {
    position: absolute;
    left: 22px;
    top: 148px;
    display: flex;
    align-items: center;
    gap: 10px;
  }
  .back-brand .brand-dot { width: 20px; height: 20px; }
  .back-brand .brand-name { font-size: 11px; line-height: 1.5; white-space: normal; width: 160px; }
  .divider {
    position: absolute;
    left: 232px;
    top: 118px;
    width: 1px;
    height: 160px;
    background: var(--red);
  }
  .contact {
    position: absolute;
    left: 254px;
    top: 126px;
    font-family: "Exo 2", sans-serif;
    font-weight: 300;
    color: var(--white);
    font-size: 13px;
    line-height: 1.45;
  }
  .contact-name {
    font-weight: 400;
    color: var(--red);
    font-size: 19px;
    letter-spacing: 0.5px;
  }
  .contact-role {
    color: var(--grey);
    font-size: 10px;
    margin-bottom: 12px;
  }
  .contact-address { margin-bottom: 12px; }
  .email-user { color: var(--red); }
</style>
</head>
<body>
<main class="stage">
  <section class="card card--front" aria-label="Business card front">
    <div class="front-brand">
      <span class="brand-dot"></span>
      <span class="brand-name">Bellwater Sound Centre</span>
    </div>
  </section>

  <section class="card card--back" aria-label="Business card back">
    <h1 class="back-heading">Bellwater Sound Centre Rehearsal<br>&amp; Recording Facilities</h1>
    <div class="back-brand">
      <span class="brand-dot"></span>
      <span class="brand-name">Bellwater Sound Centre</span>
    </div>
    <div class="divider"></div>
    <address class="contact" style="font-style:normal">
      <div class="contact-name">OWEN TAFT</div>
      <div class="contact-role">CEO</div>
      <div class="contact-address">Unit 8, 47 Marlow Street Penfield<br>NSW 2093</div>
      <div class="contact-phone">0438 915 264</div>
      <div class="contact-email"><span class="email-user">bellwatersoundcentre</span>@quillmail.example</div>
    </address>
  </section>
</main>
</body>
</html>
```